Northern Terrain Published Photographer Website

I need a website to feature a home page slide show of 6 of my top photos then a few simple pages including; gallery, bio, social, checkout, services
Updates

Need extra days to review

Target Market(s)

photography

Industry/Entity Type

Photographer

Coding

Coded - Design and coding required

Number of Pages Required

5+ page

Colors

Designer to choose colors to be used in the design.

Requirements
Must have
• clean eye catching elegant trendy
Nice to have
• unique and creative from other photographer websites

```html
<!DOCTYPE html>
<html lang="en">
<head>
<meta charset="utf-8">
<title>Northern Terrain — Photography</title>
<link href="https://fonts.googleapis.com/css2?family=Dancing+Script:wght@600&family=Lato:wght@400;700&display=swap" rel="stylesheet">
<style>
:root{
  --black:#000;
  --white:#fff;
  --ink:#222;
  --muted:#8a8a8a;
  --line:#9a9a9a;
  --hero-top:#3c3f44;
  --hero-mid:#8a5a2c;
  --hero-low:#24170e;
}
*{margin:0;padding:0;box-sizing:border-box}
html,body{width:1200px;height:3528px;overflow:hidden;background:var(--white)}
body{position:relative;font-family:'Lato',sans-serif;color:var(--ink)}
.abs{position:absolute}
.script{font-family:'Dancing Script',cursive;font-weight:600}
.photo{position:absolute;display:block}
.btn{position:absolute;border:1px solid var(--line);background:transparent;font:400 15px 'Lato',sans-serif;color:var(--ink);display:flex;align-items:center;justify-content:center}
.btn.light{border-color:var(--white);color:var(--white)}
.heading{font-size:36px;text-align:center;color:var(--ink)}
.body-copy{font-size:15px;line-height:1.6;color:var(--muted);text-align:center}

/* header + hero */
.hero{left:0;top:0;width:1200px;height:680px;background:linear-gradient(180deg,var(--hero-top) 0%,#5a4a3a 35%,var(--hero-mid) 58%,var(--hero-low) 100%)}
.topbar{left:0;top:0;width:1200px;height:72px;background:rgba(0,0,0,.55);display:flex;align-items:center;justify-content:space-between;padding:0 64px}
.logo{font-family:'Dancing Script',cursive;font-weight:600;font-size:34px;color:var(--white)}
.icons{display:flex;gap:26px}
.hero-title{left:0;width:1200px;top:320px;text-align:center;color:var(--white);font-size:34px;line-height:1.3}

/* sections */
.input{position:absolute;border:1px solid var(--line);font-size:14px;color:var(--ink);padding:12px 12px}
.tabs{left:0;width:1200px;top:1318px;display:flex;justify-content:center;gap:56px;font-size:17px}

/* footer */
.footer{left:0;top:3200px;width:1200px;height:328px;background:var(--black);color:var(--white)}
.contact{position:absolute;top:112px;width:300px;text-align:center;font-size:15px}
.contact .dot{width:36px;height:36px;border-radius:50%;background:var(--white);margin:0 auto 10px;display:flex;align-items:center;justify-content:center}
.foot-nav{position:absolute;top:236px;left:0;width:1200px;display:flex;justify-content:center;gap:46px;font-size:14px}
.copyright{position:absolute;bottom:0;left:0;width:1200px;height:40px;border-top:1px solid #333;display:flex;align-items:center;justify-content:center;font-size:13px}
</style>
</head>
<body>

<!-- Hero -->
<div class="abs hero" role="img" aria-label="Desert butte glowing orange at sunset under dark storm clouds"></div>
<header class="abs topbar">
  <svg width="22" height="18" viewBox="0 0 22 18"><path d="M1 2h20M1 9h20M1 16h20" stroke="#fff" stroke-width="2.4"/></svg>
  <div class="logo">Northern Terrain</div>
  <div class="icons">
    <svg width="20" height="20" viewBox="0 0 20 20"><circle cx="8" cy="8" r="6" stroke="#fff" stroke-width="2" fill="none"/><path d="M13 13l6 6" stroke="#fff" stroke-width="2"/></svg>
    <svg width="20" height="20" viewBox="0 0 20 20"><circle cx="10" cy="6" r="4" stroke="#fff" stroke-width="2" fill="none"/><path d="M2 19c1-5 15-5 16 0" stroke="#fff" stroke-width="2" fill="none"/></svg>
    <svg width="20" height="20" viewBox="0 0 20 20"><path d="M10 18S2 12 2 7a4 4 0 0 1 8-1 4 4 0 0 1 8 1c0 5-8 11-8 11z" stroke="#fff" stroke-width="2" fill="none"/></svg>
    <svg width="22" height="20" viewBox="0 0 22 20"><path d="M1 2h4l3 11h11l2-8H6" stroke="#fff" stroke-width="2" fill="none"/><circle cx="9" cy="17" r="1.6" fill="#fff"/><circle cx="17" cy="17" r="1.6" fill="#fff"/></svg>
  </div>
</header>
<h1 class="abs hero-title script">Seeing The World, Through the<br>Eyes of My Lens</h1>
<div class="btn light" style="left:512px;top:430px;width:176px;height:48px">Read More</div>

<!-- About -->
<h2 class="abs heading script" style="left:150px;top:836px;width:300px">About us</h2>
<p class="abs body-copy" style="left:150px;top:900px;width:300px">Lorem Ipsum is simply dummy text of the printing and typesetting industry.</p>
<p class="abs body-copy" style="left:150px;top:964px;width:300px">Lorem Ipsum has been the industry's standard so dummy text ever since the 1500s, when an known printer took a galley of type and scrambled it to make a type specimen book.</p>
<div class="btn" style="left:184px;top:1088px;width:176px;height:48px">Read More</div>
<div class="photo" style="left:484px;top:752px;width:232px;height:348px;background:linear-gradient(160deg,#e7d8b8,#b8a696 60%,#8e8c92)" role="img" aria-label="Portrait of the photographer"></div>
<div class="photo" style="left:652px;top:832px;width:352px;height:468px;background:linear-gradient(180deg,#8fc2e6 0%,#c9e1ef 45%,#7a6c5c 75%,#5b4c3e)" role="img" aria-label="Photographer walking a dog along a wooden pier by the sea"></div>

<!-- Gallery -->
<h2 class="abs heading script" style="left:0;top:1250px;width:1200px">Gallery</h2>
<nav class="abs tabs script"><span>All</span><span>Northern Terrain</span><span>Wildlife</span><span>Landscape</span><span>Sunsets/Sunrises</span></nav>
<div class="photo" style="left:80px;top:1364px;width:240px;height:236px;background:linear-gradient(180deg,#7f9a4c,#a48c56)" role="img" aria-label="Bull elk in a grassy meadow"></div>
<div class="photo" style="left:348px;top:1364px;width:500px;height:236px;background:linear-gradient(180deg,#3e2a78,#b45a9e 55%,#d9823e)" role="img" aria-label="Crystal ball on a beach at purple sunset"></div>
<div class="photo" style="left:876px;top:1364px;width:244px;height:236px;background:linear-gradient(180deg,#9bb9d6,#6c8d4e 55%,#c8c0a0)" role="img" aria-label="Waterfall below a railway bridge in autumn"></div>
<div class="photo" style="left:80px;top:1624px;width:504px;height:240px;background:linear-gradient(180deg,#a9bdd1,#c7a27c 50%,#2f6e7a)" role="img" aria-label="Canyon lake with red rock cliffs"></div>
<div class="photo" style="left:612px;top:1624px;width:236px;height:240px;background:linear-gradient(180deg,#3a3b5a,#f0b050 50%,#4a3520)" role="img" aria-label="Sunburst over desert rocks"></div>
<div class="photo" style="left:876px;top:1624px;width:244px;height:240px;background:linear-gradient(180deg,#5a6c8c,#e3b27a 55%,#6b5640)" role="img" aria-label="Mountain ridges at dusk"></div>
<div class="btn" style="left:512px;top:1900px;width:176px;height:48px">View More</div>

<!-- Services -->
<div class="photo" style="left:80px;top:2000px;width:280px;height:352px;background:linear-gradient(180deg,#c27db9,#4a6aa0 55%,#3c5a7a)" role="img" aria-label="Snow-covered pine tree at twilight"></div>
<div class="photo" style="left:248px;top:2092px;width:464px;height:340px;background:linear-gradient(180deg,#b9b4a6,#e8dcc6 55%,#a98e6a)" role="img" aria-label="Glass sphere resting on sand"></div>
<h2 class="abs heading script" style="left:780px;top:2110px;width:320px">Our Services</h2>
<p class="abs body-copy" style="left:780px;top:2172px;width:320px">Lorem Ipsum is simply dummy text of the printing and typesetting industry.</p>
<p class="abs body-copy" style="left:780px;top:2236px;width:320px">Lorem Ipsum has been the industry's standard so dummy text ever since the 1500s, when an known printer took a galley of type and scrambled it to make a type specimen book.</p>
<div class="btn" style="left:852px;top:2364px;width:172px;height:48px">Read More</div>

<!-- Contact -->
<h2 class="abs heading script" style="left:0;top:2478px;width:1200px;font-size:30px">Get In Touch</h2>
<p class="abs script" style="left:0;top:2522px;width:1200px;text-align:center;font-size:16px;color:var(--muted)">Lorem Ipsum is simply dummy text of the printing</p>
<div class="input" style="left:172px;top:2560px;width:272px;height:44px">Name</div>
<div class="input" style="left:460px;top:2560px;width:272px;height:44px">Email</div>
<div class="input" style="left:744px;top:2560px;width:268px;height:44px">Phone</div>
<div class="input" style="left:172px;top:2624px;width:840px;height:120px">Message</div>
<div class="btn" style="left:512px;top:2772px;width:176px;height:48px">Send</div>

<!-- Instagram -->
<h2 class="abs heading script" style="left:0;top:2872px;width:1200px;font-size:32px">Follow Us On Instagram</h2>
<p class="abs script" style="left:0;top:2920px;width:1200px;text-align:center;font-size:16px;color:var(--muted)">Lorem Ipsum is simply dummy text of the printing</p>
<div class="photo" style="left:80px;top:2984px;width:196px;height:188px;background:linear-gradient(180deg,#c99a6a,#8a5a38)" role="img" aria-label="Horseshoe bend canyon"></div>
<div class="photo" style="left:291px;top:2984px;width:196px;height:188px;background:linear-gradient(180deg,#8fb2d0,#a88a60)" role="img" aria-label="Wild burros in the desert"></div>
<div class="photo" style="left:502px;top:2984px;width:196px;height:188px;background:linear-gradient(180deg,#d84a2a,#3a2a2a)" role="img" aria-label="Joshua tree at red sunset"></div>
<div class="photo" style="left:713px;top:2984px;width:196px;height:188px;background:linear-gradient(180deg,#6e9bd0,#dfe6ec)" role="img" aria-label="Snowy canyon rim"></div>
<div class="photo" style="left:924px;top:2984px;width:196px;height:188px;background:linear-gradient(180deg,#a8a6a0,#6a5a48)" role="img" aria-label="Grand canyon overlook in haze"></div>

<!-- Footer -->
<footer class="abs footer">
  <div class="logo" style="position:absolute;top:24px;left:0;width:1200px;text-align:center">Northern Terrain</div>
  <div class="contact" style="left:250px">
    <div class="dot"><svg width="18" height="18" viewBox="0 0 18 18"><path d="M4 1l3 4-2 2c1 2 3 4 5 5l2-2 4 3-2 3C8 16 2 10 1 4z" fill="#000"/></svg></div>
    123. 456.7890
  </div>
  <div class="contact" style="left:450px">
    <div class="dot"><svg width="16" height="18" viewBox="0 0 16 18"><path d="M8 17S2 10 2 7a6 6 0 0 1 12 0c0 3-6 10-6 10z" fill="#000"/><circle cx="8" cy="7" r="2" fill="#fff"/></svg></div>
    123 Street, City Country,<br>Zip Code
  </div>
  <div class="contact" style="left:650px">
    <div class="dot"><svg width="18" height="14" viewBox="0 0 18 14"><rect x="1" y="1" width="16" height="12" fill="none" stroke="#000" stroke-width="2"/><path d="M1 1l8 7 8-7" fill="none" stroke="#000" stroke-width="2"/></svg></div>
    hello@northernterrain.example
  </div>
  <nav class="foot-nav"><span>Home</span><span>Bio</span><span>Gallery</span><span>Social</span><span>Checkout</span><span>Services</span></nav>
  <div class="copyright">Copyright © 2019 Northern Terrain. All Rights Reserved.</div>
</footer>

</body>
</html>
```